Nimbrel Computer Solutions
Business Technology Consulting
Professional
Gerald Pinto
1837 NE 41st Court
Palm Hollow, FL 32960
gerald@nimbrelcs.com
www.nimbrelcs.com
My company file logo. Please contact me if another format is needed.

```html
<!DOCTYPE html>
<html lang="en">
<head>
<meta charset="utf-8">
<title>Nimbrel Computer Solutions – Business Cards</title>
<link rel="stylesheet" href="https://fonts.googleapis.com/css2?family=Arimo:wght@400;700&display=swap">
<style>
  :root {
    --page-bg: #e9e6e1;
    --card-white: #ffffff;
    --card-shade: #e2e4e8;
    --brand-blue: #1b4f8c;
    --brand-blue-light: #2f7fc4;
    --brand-gold: #c9a227;
    --ink: #1f1f1f;
    --ink-soft: #3a3a3a;
    --divider: #9aa0a6;
  }
  html, body {
    margin: 0;
    padding: 0;
    width: 1200px;
    height: 902px;
    overflow: hidden;
    background: var(--page-bg);
    font-family: "Arimo", Arial, sans-serif;
  }
  .canvas { position: relative; width: 1200px; height: 902px; }
  .card {
    position: absolute;
    width: 558px;
    height: 320px;
    border-radius: 14px;
    overflow: hidden;
    background: linear-gradient(135deg, var(--card-white) 0%, var(--card-white) 50%, var(--card-shade) 100%);
    box-shadow: 0 4px 14px rgba(0,0,0,0.2);
  }
  .card-front { left: 159px; top: 154px; }
  .card-back  { left: 447px; top: 442px; }

  /* Front */
  .brand-block {
    position: absolute;
    left: 33px;
    top: 78px;
    width: 260px;
    text-align: center;
  }
  .brand-dot {
    display: block;
    width: 76px;
    height: 76px;
    margin: 0 auto;
    border-radius: 50%;
    background: radial-gradient(circle at 35% 30%, var(--brand-blue-light), var(--brand-blue) 70%);
  }
  .brand-name {
    margin: 20px 0 0;
    color: var(--brand-blue);
    font-weight: 700;
    font-size: 48px;
    letter-spacing: 1px;
    line-height: 1;
  }
  .brand-tagline {
    margin: 4px 0 0;
    color: var(--brand-blue);
    font-weight: 700;
    font-size: 11.5px;
    letter-spacing: 2.4px;
  }
  .front-divider {
    position: absolute;
    left: 305px;
    top: 83px;
    width: 1px;
    height: 160px;
    background: var(--divider);
  }
  .contact {
    position: absolute;
    left: 330px;
    top: 86px;
    color: var(--ink-soft);
    font-size: 12.5px;
    line-height: 17px;
  }
  .contact p { margin: 0; }
  .contact .contact-name {
    margin: 0 0 22px;
    color: var(--ink);
    font-size: 20px;
    line-height: 24px;
    font-weight: 700;
  }
  .contact .gap { margin-top: 10px; }
  .front-band {
    position: absolute;
    left: 0;
    bottom: 0;
    width: 558px;
    height: 22px;
  }
  .front-band svg { display: block; }
  .band-url {
    position: absolute;
    right: 28px;
    bottom: 4px;
    color: var(--ink);
    font-size: 11.5px;
    letter-spacing: 1.2px;
  }

  /* Back */
  .back-watermark {
    position: absolute;
    left: -7px;
    top: 59px;
    width: 292px;
    height: 292px;
    border-radius: 50%;
    background: radial-gradient(circle, rgba(200,205,212,0.45), rgba(220,224,230,0.15) 70%);
  }
  .back-brand {
    position: absolute;
    left: 395px;
    top: 190px;
    width: 160px;
    text-align: center;
  }
  .back-brand .brand-dot { width: 80px; height: 80px; }
  .back-url {
    margin: 10px 0 0;
    color: var(--ink-soft);
    font-size: 12.5px;
    letter-spacing: 1px;
  }
</style>
</head>
<body>
<main class="canvas">

  <section class="card card-front" aria-label="Business card front">
    <div class="brand-block">
      <span class="brand-dot"></span>
      <p class="brand-name">NIMBREL</p>
      <p class="brand-tagline">COMPUTER SOLUTIONS</p>
    </div>

    <div class="front-divider"></div>

    <div class="contact">
      <p class="contact-name">Gerald Pinto</p>
      <p>1837 NE 41st Court</p>
      <p>Palm Hollow, FL 32960</p>
      <p class="gap">Phone: 555-318-0147</p>
      <p>Email: gerald@nimbrelcs.com</p>
    </div>

    <div class="front-band">
      <svg width="558" height="22" viewBox="0 0 558 22">
        <defs>
          <linearGradient id="bandBlue" x1="0" y1="0" x2="0" y2="1">
            <stop offset="0" stop-color="#2f7fc4"/>
            <stop offset="1" stop-color="#1b4f8c"/>
          </linearGradient>
          <linearGradient id="bandGold" x1="0" y1="0" x2="0" y2="1">
            <stop offset="0" stop-color="#e2c45a"/>
            <stop offset="1" stop-color="#b58e1c"/>
          </linearGradient>
        </defs>
        <rect x="0" y="8" width="558" height="14" fill="url(#bandBlue)"/>
        <polygon points="338,22 353,0 558,0 558,22" fill="url(#bandGold)"/>
      </svg>
      <span class="band-url">www.nimbrelcs.com</span>
    </div>
  </section>

  <section class="card card-back" aria-label="Business card back">
    <div class="back-watermark" role="img" aria-label="Faint brand circle"></div>
    <div class="back-brand">
      <span class="brand-dot"></span>
      <p class="back-url">www.nimbrelcs.com</p>
    </div>
  </section>

</main>
</body>
</html>
```